Cosmetics Brand Logo and Bottle Label Design

We are creating a new cosmetics brand called "Nolan Whitby" and would like you to create an amazing logo and bottle label for this brand's new 100% pure argan oil product.
For the logo, we really like the logo's of Marin Calloway and Vessa. The text should be Sans Serif (without feet).
For the actual bottle label, please find attached labels of one of our competitors design which really like. We really like the simplicity and elegance of the design. The only difference is that our product will be using light turqoise as the brand color. Please feel free to add your own creativity into it as well.
Industry/Entity Type
Cosmetics
Logo Text
Nolan Whitby
Font styles to use

```html
<!DOCTYPE html>
<html lang="en">
<head>
<meta charset="utf-8">
<title>Nolan Whitby – Argan Oil Label</title>
<link rel="stylesheet" href="https://fonts.googleapis.com/css2?family=Lato:wght@300;400&display=swap">
<style>
  :root {
    --backdrop: #ece3e1;
    --label-turquoise: #66c5b0;
    --tint-light: #a3ddd0;
    --tint-line: #93d6c6;
    --ink-white: #ffffff;
    --ink-dark: #2f4a45;
    --stamp-teal: #3bb5a3;
  }
  html, body {
    margin: 0;
    padding: 0;
    width: 1200px;
    height: 1200px;
    overflow: hidden;
    background: var(--backdrop);
  }
  .canvas {
    position: relative;
    width: 1200px;
    height: 1200px;
  }
  .label {
    position: absolute;
    left: 40px;
    top: 250px;
    width: 1120px;
    height: 700px;
    display: block;
  }
  .label__ground { fill: var(--label-turquoise); }
  .brand-name {
    font-family: "Lato", sans-serif;
    font-weight: 300;
    font-size: 84px;
    fill: var(--ink-white);
  }
  .product-line {
    font-family: "Lato", sans-serif;
    font-weight: 300;
    font-size: 48px;
    fill: var(--tint-light);
  }
  .descriptor {
    font-family: "Lato", sans-serif;
    font-weight: 300;
    font-size: 40px;
    fill: var(--tint-light);
  }
  .volume {
    font-family: "Lato", sans-serif;
    font-weight: 400;
    font-size: 35px;
    fill: var(--ink-white);
  }
  .leaf-mark { fill: #72cab6; stroke: var(--tint-line); stroke-width: 1; }
  .info-frame, .info-box { fill: none; stroke: var(--tint-line); stroke-width: 1; }
  .info-copy {
    font-family: "Lato", sans-serif;
    font-weight: 400;
    font-size: 9.6px;
    fill: var(--ink-dark);
  }
  .placeholder-stamp {
    font-family: "Lato", sans-serif;
    font-weight: 400;
    font-size: 40px;
    fill: var(--stamp-teal);
  }
</style>
</head>
<body>
<main class="canvas">
  <svg class="label" viewBox="0 0 1008 630" xmlns="http://www.w3.org/2000/svg">
    <rect class="label__ground" x="0" y="0" width="1008" height="630"/>

    <text class="brand-name" x="0" y="0" transform="translate(213 575) rotate(-90)" textLength="525" lengthAdjust="spacingAndGlyphs">NOLAN WHITBY</text>
    <text class="product-line" x="0" y="0" transform="translate(277 490) rotate(-90)" textLength="393" lengthAdjust="spacingAndGlyphs">100% Pure Argan Oil</text>

    <rect class="leaf-mark" x="332" y="228" width="158" height="192" rx="60" role="img" aria-label="Line illustration of argan leaves and fruit"/>

    <text class="descriptor" x="306" y="482">organic</text>
    <text class="descriptor" x="306" y="528">moisturizing oil</text>
    <text class="volume" x="306" y="578">50ml  1.7 fl oz</text>

    <rect class="info-frame" x="752" y="68" width="163" height="497"/>
    <rect class="info-box" x="920" y="90" width="62" height="102"/>

    <g class="info-copy">
      <text transform="translate(770 553) rotate(-90)">We are creating a new cosmetics brand called "Nolan Whitby" and would like you to create an</text>
      <text transform="translate(783 553) rotate(-90)">amazing logo and bottle label for this brand's new 100% pure argan oil product.</text>
      <text transform="translate(818 553) rotate(-90)">For the logo, we really like the logo's of Marin Calloway and Vessa. The text should be Sans Serif</text>
      <text transform="translate(831 553) rotate(-90)">(without feet).</text>
      <text transform="translate(866 553) rotate(-90)">For the actual bottle label, please find attached labels of one of our competitors design which</text>
      <text transform="translate(879 553) rotate(-90)">really like. We really like the simplicity and elegance of the design. The only difference is that our</text>
      <text transform="translate(892 553) rotate(-90)">product will be using light turqoise as the brand color. Please feel free to add your own creativity</text>
      <text transform="translate(905 553) rotate(-90)">into it as well.</text>
    </g>

    <text class="placeholder-stamp" transform="translate(832 508) rotate(-73)">DUMMY TEXTS</text>
  </svg>
</main>
</body>
</html>
```